Web Design Project

Goal
Combine 2 sites into 1 and enhance functionality

Concept & Overview

My current websites are rowanvoices dot com and tidewaterguides dot org. They are not very popular but I run ads and capture leads and do a tidy bit, but I am going on tour and need to have my website upgrade.

My goal is to redesign rowanvoices and have it as a 10 page site that introduces me and also capture leads in an effective manner then introduce a 5 page system.

I need to update the layout and feel of the site to match the color and image of the book. Currently the book is at tidewaterguides.org and my speaking is at rowanvoices.com. I need the two to combine but I also need functionality to improve. I introduce a 5 step system and I think a visual image like this one can better introduce it.

Here: https://www.brightleafmedia.com/packages/kgt-marla-quinns-life-improvement-program.html

Then in there I need the Lesson Area

Like:

https://www.brightleafmedia.com/packages/kgt-marla-quinns-life-improvement-program.html

They are few samples I can show but this is the main concept.

Target Market(s)

Schools, colleges, churches, and youth organizations

Industry/Entity Type

Tour

Requirements
Must have
• A clean wide home page that is properly designed can do the job of leading to the optin without the sales look.

Nice to have
• https://www.brightleafmedia.com/packages/kgt-marla-quinns-life-improvement-program.html
Should not have
• Sales look and feel

```html
<!DOCTYPE html>
<html lang="en">
<head>
<meta charset="utf-8">
<title>Rowan Ellery – Youth Expert, Motivational Speaker and Author</title>
<link href="https://fonts.googleapis.com/css2?family=Arimo:ital,wght@0,400;0,700;1,400;1,700&family=Lato:wght@400;700&family=Open+Sans:wght@600&family=Permanent+Marker&display=swap" rel="stylesheet">
<style>
:root{
  --navy:#2c3e5c;
  --ink:#24324d;
  --sky:#3aa9dd;
  --sky-dark:#2a93c8;
  --page:#e8eef0;
  --white:#ffffff;
  --text:#2a2f38;
  --tile-shadow:rgba(0,0,0,.28);
}
*{margin:0;padding:0;box-sizing:border-box}
html,body{width:839px;height:1200px;overflow:hidden}
body{position:relative;background:var(--page);font-family:"Arimo",Arial,sans-serif;color:var(--text)}
.abs{position:absolute}

/* top bar */
.topbar{left:0;top:0;width:839px;height:65px;background:var(--navy)}
.topbar .tagline{left:173px;top:23px;width:260px;color:var(--white);font-size:8.4px;font-style:italic;line-height:11px}
.topbar .tagline b{font-style:normal}
.topbar .phone{left:503px;top:19px;color:var(--white);font-size:22px;font-weight:700;display:flex;align-items:center;gap:8px}

/* masthead */
.masthead{left:0;top:65px;width:839px;height:82px;background:var(--white);text-align:center}
.masthead .name{margin-top:15px;font-size:37px;line-height:38px;color:var(--sky);letter-spacing:.5px}
.masthead .role{font-size:14px;color:var(--ink);margin-top:0}
.stripe{left:0;top:147px;width:839px;height:8px;background:var(--sky)}

/* navigation */
.nav{left:172px;top:155px;width:494px;height:51px;display:flex;gap:1px;background:var(--page)}
.nav a{flex:1;background:var(--white);color:var(--ink);text-decoration:none;font-size:11px;display:flex;align-items:center;justify-content:center;text-align:center;line-height:12px}
.nav a.current{background:var(--sky);color:var(--white);font-weight:700}

/* hero */
.hero{left:172px;top:229px;width:494px;height:206px;background:linear-gradient(160deg,#6b5544 0%,#3a2e28 45%,#1f1a18 100%);box-shadow:0 10px 12px -6px rgba(0,0,0,.45)}
.hero .headline{position:absolute;left:200px;top:40px;color:var(--white);font-family:"Open Sans",sans-serif;font-weight:600;font-size:13px;line-height:16px;text-transform:uppercase;background:rgba(30,28,30,.55);padding:8px 10px;border-radius:6px;width:280px}
.hero .headline big{font-size:15px}
.hero .quote{position:absolute;left:0;right:0;bottom:4px;color:var(--white);font-family:"Permanent Marker",cursive;font-size:9.6px;text-transform:uppercase;text-align:right;padding-right:6px;line-height:11px}

/* feature tiles */
.feature{width:147px}
.feature .art{width:147px;height:126px;background:var(--white);padding:8px;box-shadow:0 2px 4px var(--tile-shadow)}
.feature .art div{width:100%;height:100%}
.feature h2{font-family:"Lato",sans-serif;font-weight:400;font-size:10px;color:var(--ink);text-align:center;margin-top:10px;letter-spacing:.3px}
.feature p{font-size:6.1px;line-height:8.4px;margin-top:5px;color:var(--text)}
.feature p.voice{font-style:italic}
.more{width:22px;height:22px;border-radius:50%;background:var(--sky);color:var(--white);font-family:"Lato",sans-serif;font-weight:700;font-size:5.6px;display:flex;align-items:center;justify-content:center;border:1.5px solid var(--white);box-shadow:0 1px 2px rgba(0,0,0,.25)}

.divider{left:172px;top:990px;width:494px;height:4px;background:var(--sky)}

/* info columns */
.info h3{font-size:10px;font-weight:400;color:var(--ink);line-height:11px}
.info h4{font-size:7px;font-weight:400;color:var(--sky);margin-top:1px}
.info p{font-size:5.4px;line-height:7.6px;margin-top:6px}
.info .mentoring-title{font-size:7.6px;line-height:8.4px}
.btn{display:inline-block;background:linear-gradient(var(--sky),var(--sky-dark));color:var(--white);font-size:6px;font-weight:700;padding:4px 10px;border-radius:3px;width:60px;text-align:center;box-shadow:0 1px 2px rgba(0,0,0,.2)}
.contact .tel{font-size:13px;color:var(--sky);margin-top:3px}
.contact .mail{font-size:8px;color:var(--ink)}

/* footer */
.footer{left:0;top:1156px;width:839px;height:44px;background:var(--white)}
.footer .copy{position:absolute;left:173px;top:22px;font-size:5.5px;color:var(--sky)}
.footer .social{position:absolute;left:551px;top:12px;display:flex;gap:6px}
.footer .social span{width:19px;height:19px;border-radius:3px;background:#9aa8b8}
</style>
</head>
<body>

<header>
  <div class="abs topbar">
    <p class="abs tagline">From a high school <b>dropout</b> to a high school <b>valedictorian</b>,<br>Rowan's goal is to show students how to get <b>BACK ON TRACK</b></p>
    <p class="abs phone">
      <svg width="14" height="16" viewBox="0 0 14 16" aria-hidden="true"><path d="M3 1 L5.5 1 L6.5 5 L4.6 6.3 C5.4 8.6 6.8 10.4 8.6 11.6 L10 9.8 L13.5 11 L13.5 13.6 C13.5 14.6 12.6 15.2 11.6 15 C6.4 14 2 9.4 1.2 3.8 C1 2.2 1.8 1 3 1 Z" fill="#3aa9dd"/></svg>
      (555) 214-0387
    </p>
  </div>
  <div class="abs masthead">
    <h1 class="name">ROWAN ELLERY</h1>
    <p class="role">YOUTH EXPERT, MOTIVATIONAL SPEAKER AND AUTHOR</p>
  </div>
  <div class="abs stripe"></div>
  <nav class="abs nav">
    <a class="current" href="#">Home</a>
    <a href="#">About</a>
    <a href="#">Speaking</a>
    <a href="#">Products &amp;<br>Services</a>
    <a href="#">Rowan's<br>Blog</a>
    <a href="#">Customer<br>Testimonials</a>
    <a href="#">Contact</a>
  </nav>
</header>

<main>
  <section class="abs hero" role="img" aria-label="Photo of Rowan speaking to a seated audience in a conference room">
    <p class="headline"><big>Rowan Ellery</big><br>Inspires people to look at their talents and turn them into possibilities</p>
    <p class="quote">"...You have to let go of people with your problems and find friends who know your solution"<br>- Rowan Ellery</p>
  </section>

  <article class="abs feature" style="left:174px;top:467px">
    <div class="art"><div role="img" aria-label="Illustration of overlapping blue speech bubbles" style="background:radial-gradient(circle,#4aa8e0 0%,#8cc8ee 45%,#fff 72%)"></div></div>
    <h2>SPEAKING</h2>
    <p>Rowan Ellery inspires over 100,000 people a month to grow stronger in their lives and dreams while giving more intelligently and consistently to their teams and communities. He's shared the stage with some of the most respected teachers and leaders of our age.</p>
  </article>
  <div class="abs more" style="left:297px;top:682px">MORE</div>

  <article class="abs feature" style="left:347px;top:467px">
    <div class="art"><div role="img" aria-label="Illustration of hands with hearts arranged in a circle" style="background:radial-gradient(circle,#3f8fcf 0%,#6fb6e6 40%,#fff 70%)"></div></div>
    <h2>MENTORING</h2>
    <p class="voice">“I can relate to most students struggling with self-confidence and who have gone off course. My background as an educator, teacher and counselor gives me the tools needed to help students. Also my history as a gang member, high school drop out and high school valedictorian makes it easier for students to relate to me.” ~Rowan E.</p>
  </article>
  <div class="abs more" style="left:470px;top:682px">MORE</div>

  <article class="abs feature" style="left:519px;top:467px">
    <div class="art"><div role="img" aria-label="Illustration of a speaker silhouette in front of an audience" style="background:linear-gradient(#fff 0%,#7fbde8 35%,#3a8fcc 65%,#2c3e5c 100%)"></div></div>
    <h2>SEMINARS AND WORKSHOPS</h2>
    <p>Rowan Ellery's seminars have become famous for two things: comprehensive and actionable content, and personal transformation. He is the rare trainer capable of coupling personal growth with professional development, which is why colleges and business organizations invite him to their stages.</p>
  </article>
  <div class="abs more" style="left:642px;top:682px">MORE</div>

  <article class="abs feature" style="left:174px;top:726px">
    <div class="art"><div role="img" aria-label="Illustration of a stylised blue tree with flowers" style="background:radial-gradient(circle,#2e6aa6 0%,#4aa8e0 40%,#fff 70%)"></div></div>
    <h2>ROWAN'S BLOG</h2>
    <p>A collection of personal tips &amp; tricks to help you gain success of your life and help you embrace your past and move through it. When youth and young adults understand the importance of courage, they can see challenges differently. The key is to stop making excuses, regain your focus in life, and push forward.</p>
  </article>
  <div class="abs more" style="left:297px;top:941px">MORE</div>

  <article class="abs feature" style="left:347px;top:726px">
    <div class="art"><div role="img" aria-label="Illustration of two chat bubbles, one with an exclamation mark and one smiling" style="background:linear-gradient(120deg,#fff 5%,#2c3e5c 30%,#2c3e5c 45%,#4aa8e0 60%,#fff 92%)"></div></div>
    <h2>TESTIMONIALS</h2>
    <p class="voice">“It was a true inspiration work with Rowan as he guides our students to bring out the best in themselves. The team really has found hope and the program was a true success.”</p>
    <p style="font-weight:700;margin-top:6px">Dr. Lena Marsh<br>Crestfield University School of Communication</p>
  </article>
  <div class="abs more" style="left:470px;top:941px">MORE</div>

  <article class="abs feature" style="left:519px;top:726px">
    <div class="art"><div role="img" aria-label="Product photo of the book, workbook and disc set" style="background:linear-gradient(135deg,#fff 0%,#9cc9ea 30%,#2f6fb0 60%,#e9eef3 100%)"></div></div>
    <h2>LIFE'S OPEN ROAD</h2>
    <p><b>Life's Open Road</b> the inspirational story of MJ, a young man struggling with realizing his full potential. After getting into a fight at school, MJ begins to reprioritize his goals and reevaluate where he wants his life to go. He joins a leadership course initially to earn an easy A, but soon forms a bond with a mentor while on a class trip.</p>
  </article>
  <div class="abs more" style="left:642px;top:941px">MORE</div>

  <div class="abs divider"></div>

  <section class="abs info" style="left:173px;top:1019px;width:215px">
    <h3>ROWAN ELLERY -</h3>
    <h4>YOUTH EXPERT, MOTIVATIONAL SPEAKER AND AUTHOR</h4>
    <p>Rowan is a youth expert, an author, youth motivational speaker and teen leader who understands the journey of many students today. The former gang member and high school drop out understands the challenges faced by students who are seeking approval and acceptance. His journey from gang member to high school teacher was long but gave empowerment and challenges students to make choices, build character and live their best life.</p>
    <p style="margin-top:4px">His story of an outstanding student who followed the wrong crowd is common today. Given a second chance at high school, Rowan got his act together and graduated Valedictorian and speaks today at school assemblies, conferences and organizations this message of hope. A dynamic story that every student will love.</p>
  </section>

  <section class="abs info" style="left:422px;top:1019px;width:140px">
    <h3 class="mentoring-title">2-DAYS PARENT-TEEN<br>MENTORING PROGRAM</h3>
    <p style="margin-top:10px">Treat yourselves to an amazing day of learning and inspiration with your son or daughter. This Program is custom planned for each client with options to focus on personal performance, goal setting, developing personal style and becoming the leader of your life.</p>
    <span class="btn" style="margin-top:9px">SIGN UP NOW</span>
  </section>

  <section class="abs info contact" style="left:577px;top:1019px;width:100px">
    <h3>CONTACT US</h3>
    <p class="tel">(555) 214-0387</p>
    <p class="mail" style="margin-top:0;line-height:10px">rowan@brightpathyouth.com</p>
    <span class="btn" style="margin-top:4px">BOOK ROWAN</span>
    <p style="margin-top:6px">Get Rowan's FREE ebook on helping teens and updates on event and special offers.</p>
    <span class="btn" style="margin-top:6px">SIGN UP NOW</span>
  </section>
</main>

<footer class="abs footer">
  <p class="copy">Copyright Rowan Ellery 2012</p>
  <div class="social" aria-label="Social links">
    <span></span><span></span><span></span><span></span><span></span>
  </div>
</footer>

</body>
</html>
```